Clarinet Past Midnight: mini recital & soiree

I need a poster design for a recital I'm doing next Friday April 25. It's an "after party" from 10 - 1am where I'll be playing a 30 min program followed by a DJ and there'll be food wine etc. I want to see a very "sexy" kind of poster. Modern with a "south beach" kind of art deco feel but without the really cheesy connotation that south beach sometimes has (if that makes any sense). I've included the link for the Gatherlink event so you can get an idea of the feel I want.

Cheers!

https://www.gatherlink.example/events/519304762811095/

Target Market(s)

College Students at the Coral Ridge Institute

South Beach-ians

Industry/Entity Type

Events

Colors

Designer to choose colors to be used in the design.

Requirements
Must have
• Title of event..
Date..
Location..
Food / Beverage served..
DJ Torvik..

```html
<!DOCTYPE html>
<html lang="en">
<head>
<meta charset="utf-8">
<title>Clarinet Past Midnight — Mini Recital &amp; Soirée</title>
<link href="https://fonts.googleapis.com/css2?family=Oswald:wght@500&family=Poiret+One&family=Quicksand:wght@400;500;600&display=swap" rel="stylesheet">
<style>
  :root {
    --canvas: #e9e9e9;
    --paper: #ffffff;
    --night: #0b0710;
    --ink: #111111;
    --white: #ffffff;
    --cream: #efede4;
    --silver: #b9b9bc;
    --lime: #9cc63b;
    --violet: #a06ab0;
    --plum: #8b3a8f;
    --coral: #f2734f;
    --sky: #9fd3f2;
    --chartreuse: #c8d84a;
    --peach: #f6a58a;
  }
  * { margin: 0; padding: 0; box-sizing: border-box; }
  html, body { width: 1200px; height: 1152px; overflow: hidden; background: var(--canvas); }
  .poster {
    position: absolute; left: 210px; top: 23px;
    width: 780px; height: 1106px;
    background: var(--night); overflow: hidden;
  }
  .header-band { position: absolute; left: 0; top: 0; width: 780px; height: 181px; background: var(--paper); }
  .night-glow {
    position: absolute; left: 0; top: 181px; width: 780px; height: 925px;
    background:
      radial-gradient(ellipse 45% 20% at 75% 12%, rgba(210,70,40,.45), transparent 70%),
      radial-gradient(ellipse 55% 25% at 60% 48%, rgba(150,40,70,.35), transparent 70%),
      radial-gradient(ellipse 40% 18% at 80% 78%, rgba(120,30,50,.3), transparent 70%),
      radial-gradient(ellipse 60% 40% at 50% 30%, rgba(60,40,90,.35), transparent 75%),
      var(--night);
  }
  .art { position: absolute; left: 0; top: 0; }
  .title-kicker {
    position: absolute; left: 31px; top: 80px;
    font-family: "Quicksand", sans-serif; font-weight: 500;
    font-size: 31px; letter-spacing: 1px; color: var(--plum);
  }
  .title-line {
    position: absolute; right: 20px;
    font-family: "Poiret One", sans-serif; line-height: 1;
    text-align: right; white-space: nowrap;
  }
  .title-past { top: 62px; font-size: 140px; color: var(--ink); letter-spacing: 4px; }
  .title-midnight { top: 186px; font-size: 96px; color: var(--white); letter-spacing: 2px; }
  .event-name {
    position: absolute; right: 50px; top: 494px;
    font-family: "Oswald", sans-serif; font-weight: 500;
    font-size: 50px; color: var(--white); text-transform: uppercase;
  }
  .event-live {
    position: absolute; right: 50px; top: 562px;
    font-family: "Quicksand", sans-serif; font-weight: 400;
    font-size: 32px; color: var(--coral); letter-spacing: 1px;
  }
  .dj-name {
    position: absolute; right: 50px; top: 614px;
    font-family: "Quicksand", sans-serif; font-weight: 600;
    font-size: 54px; color: var(--white); letter-spacing: 1px;
  }
  .dj-note {
    position: absolute; right: 50px; top: 680px;
    font-family: "Quicksand", sans-serif; font-weight: 500;
    font-size: 16px; color: var(--coral); letter-spacing: 1.5px;
  }
  .details { position: absolute; right: 50px; top: 1000px; text-align: right; font-family: "Quicksand", sans-serif; white-space: nowrap; }
  .details-date { font-size: 23px; font-weight: 500; color: var(--sky); letter-spacing: .3px; }
  .details-venue { font-size: 13px; font-weight: 500; color: var(--peach); letter-spacing: 1px; margin-top: 4px; }
  .details-menu { font-size: 13px; font-weight: 500; color: var(--chartreuse); letter-spacing: 1px; margin-top: 4px; }
</style>
</head>
<body>
  <main class="poster">
    <div class="header-band"></div>
    <div class="night-glow" role="img" aria-label="Blurred night-time city lights in red, orange and violet"></div>

    <svg class="art" width="780" height="1106" viewBox="0 0 780 1106">
      <defs>
        <radialGradient id="instrumentTone" cx="0.35" cy="0.55" r="0.7">
          <stop offset="0" stop-color="var(--silver)"/>
          <stop offset="0.6" stop-color="#d6d5cf"/>
          <stop offset="1" stop-color="var(--cream)"/>
        </radialGradient>
      </defs>
      <polygon class="band-violet" fill="var(--violet)" points="0,181 70,181 295,300 280,430 285,560 350,665 300,890 282,1010 257,1106 0,1106"/>
      <polygon class="band-lime" fill="var(--lime)" points="0,181 55,181 282,300 267,430 272,560 335,663 285,890 267,1010 242,1106 0,1106"/>
      <polygon class="instrument-photo" fill="url(#instrumentTone)" role="img" aria-label="Photograph of a silver clarinet on a cream cut-out"
               points="0,200 40,181 255,181 255,300 245,430 250,560 318,660 268,890 250,1010 224,1106 0,1106"/>
    </svg>

    <div class="title-kicker">CLARINET</div>
    <div class="title-line title-past">PAST</div>
    <div class="title-line title-midnight">MIDNIGHT</div>

    <div class="event-name">Mini Recital &amp; Soirée</div>
    <div class="event-live">LIVE</div>

    <div class="dj-name">DJ TORVIK</div>
    <div class="dj-note">DJ SET FOR THE NIGHT</div>

    <div class="details">
      <p class="details-date">FRIDAY, APRIL 25 AT 10:00PM - 1:00AM</p>
      <p class="details-venue">HARLOW ALUMNI CENTER- CORAL RIDGE INSTITUTE</p>
      <p class="details-menu">FOOD / WINE / DRINK WILL BE SERVED!!</p>
    </div>
  </main>
</body>
</html>
```